Evaporative Air Conditioning Summer Service

Would like to design a flyer to send out in an email to existing clients to promote a Pre-summer service for Evaporative Air Conditioners
Cost will be $110.00 inc gst
Tasks included in service are
- Inspection and clean of pads
- Inspection and check float valve, water pump, fan, motor, bearings, drain
- Clean basin
- Supply of bacterial tablet
- Inspect overall condition of unit
- Any repairs if required will be quoted
Please see files attached of a previous very basic flyer I have used for installation and replacement unit costs. This has current contact information
Have also uploaded company logo for use.
Thanks

```html
<!DOCTYPE html>
<html lang="en">
<head>
<meta charset="utf-8">
<title>Pre-Summer Service for Evaporative Air Conditioners</title>
<link rel="stylesheet" href="https://fonts.googleapis.com/css2?family=Bebas+Neue&family=Fira+Sans+Condensed:wght@500;600&family=Fira+Sans:wght@400&family=Montserrat:wght@400;700;800&display=swap">
<style>
  :root {
    --sky-top: #0b5fae;
    --sky-mid: #3d9fcb;
    --sky-light: #b9e2ee;
    --sky-pale: #dcf1f7;
    --navy: #14388f;
    --blue: #2a8ce6;
    --list-ink: #1b3f97;
    --orange-left: #e8663a;
    --orange-right: #f4b03c;
    --white: #ffffff;
  }
  * { margin: 0; padding: 0; box-sizing: border-box; }
  html, body { width: 894px; height: 1200px; overflow: hidden; background: #f2f3f5; }
  .flyer {
    position: relative; width: 894px; height: 1200px; overflow: hidden;
    background: linear-gradient(180deg, var(--sky-top) 0%, var(--sky-mid) 28%, var(--sky-light) 52%, var(--sky-pale) 75%, #eef9fb 100%);
    font-family: "Fira Sans", sans-serif;
  }
  .headline {
    position: absolute; top: 52px; left: 0; width: 100%;
    text-align: center; color: var(--white);
    font-family: "Bebas Neue", sans-serif; font-size: 76px; line-height: 78px;
    text-shadow: 0 3px 6px rgba(0,0,0,0.25);
  }
  .price-badge {
    position: absolute; left: 70px; top: 226px; width: 234px; height: 226px; border-radius: 50%;
    background: radial-gradient(circle at 65% 40%, var(--blue) 0%, #1c5fc4 45%, var(--navy) 100%);
    box-shadow: 0 14px 24px rgba(20,60,120,0.25);
  }
  .price-badge__ring {
    position: absolute; inset: 9px; border: 2px solid var(--white); border-radius: 50%;
    display: flex; flex-direction: column; align-items: center; justify-content: center;
    color: var(--white); font-family: "Fira Sans Condensed", sans-serif; font-weight: 600;
  }
  .price-badge__lead { font-size: 32px; line-height: 36px; }
  .price-badge__amount { font-size: 52px; line-height: 52px; }
  .price-badge__note { font-size: 28px; line-height: 34px; }
  .tasks-heading {
    position: absolute; left: 343px; top: 232px; width: 467px; height: 44px;
    padding-left: 14px; line-height: 44px; color: var(--white);
    font-family: "Fira Sans Condensed", sans-serif; font-weight: 600; font-size: 27px;
    background: linear-gradient(90deg, var(--orange-left) 0%, var(--orange-right) 80%, rgba(244,176,60,0) 100%);
  }
  .task-list { position: absolute; left: 363px; top: 298px; list-style: none; color: var(--list-ink); }
  .task-list li { position: relative; padding-left: 37px; font-size: 24px; line-height: 36.6px; width: 480px; }
  .task-list svg { position: absolute; left: 0; top: 10px; width: 16px; height: 16px; }
  .unit-art {
    position: absolute; left: 168px; top: 578px; width: 580px; height: 360px;
    border-radius: 16px 16px 0 0;
    background: linear-gradient(180deg, #f6f7f8 0%, #e6eaec 50%, rgba(200,238,244,0.7) 54%, rgba(215,244,240,0.4) 100%);
  }
  .base-shapes { position: absolute; left: 0; top: 0; }
  .brand {
    position: absolute; left: 560px; top: 972px; width: 310px; display: flex; align-items: center; gap: 12px;
    color: var(--navy); font-family: "Montserrat", sans-serif; font-weight: 800; font-size: 22px; line-height: 28px;
  }
  .brand__dot { flex: none; width: 26px; height: 26px; border-radius: 50%; background: var(--navy); }
  .contact-art {
    position: absolute; left: 116px; top: 936px; width: 81px; height: 71px; border-radius: 8px;
    background: linear-gradient(180deg, rgba(255,255,255,0.55), rgba(255,255,255,0.3));
  }
  .contact-tab {
    position: absolute; left: 0; top: 1018px; width: 275px; height: 40px;
    background: linear-gradient(90deg, var(--navy), #2457c0);
    clip-path: polygon(0 0, 100% 0, 94% 100%, 0 100%);
    color: var(--white); font-family: "Montserrat", sans-serif; font-weight: 800; font-size: 23px;
    line-height: 40px; padding-left: 58px;
  }
  .contact-lines { position: absolute; left: 0; top: 1060px; color: var(--white); font-family: "Montserrat", sans-serif; white-space: nowrap; }
  .contact-line { position: relative; padding-left: 100px; }
  .contact-line svg { position: absolute; left: 61px; }
  .contact-line--phone { font-weight: 700; font-size: 38px; line-height: 46px; letter-spacing: 2px; }
  .contact-line--phone svg { top: 11px; width: 24px; height: 24px; }
  .contact-line--email { font-size: 28px; line-height: 34px; margin-top: 3px; }
  .contact-line--email svg { top: 6px; width: 22px; height: 22px; }
  .contact-line--abn { font-size: 27px; line-height: 33px; }
</style>
</head>
<body>
<main class="flyer">
  <h1 class="headline">Pre-Summer Service for<br>Evaporative Air Conditioners</h1>

  <div class="price-badge">
    <div class="price-badge__ring">
      <span class="price-badge__lead">Cost will be</span>
      <span class="price-badge__amount">$110.00</span>
      <span class="price-badge__note">including GST</span>
    </div>
  </div>

  <h2 class="tasks-heading">Tasks included in service are</h2>
  <ul class="task-list">
    <li><svg viewBox="0 0 16 16"><rect x="1" y="1" width="14" height="14" fill="none" stroke="currentColor" stroke-width="1.4"/><path d="M4 8l3 3 6-8" fill="none" stroke="currentColor" stroke-width="1.6"/></svg>Inspection and clean of pads</li>
    <li><svg viewBox="0 0 16 16"><rect x="1" y="1" width="14" height="14" fill="none" stroke="currentColor" stroke-width="1.4"/><path d="M4 8l3 3 6-8" fill="none" stroke="currentColor" stroke-width="1.6"/></svg>Inspection and check float valve, water pump, fan, motor, bearings, drain</li>
    <li><svg viewBox="0 0 16 16"><rect x="1" y="1" width="14" height="14" fill="none" stroke="currentColor" stroke-width="1.4"/><path d="M4 8l3 3 6-8" fill="none" stroke="currentColor" stroke-width="1.6"/></svg>Clean basin</li>
    <li><svg viewBox="0 0 16 16"><rect x="1" y="1" width="14" height="14" fill="none" stroke="currentColor" stroke-width="1.4"/><path d="M4 8l3 3 6-8" fill="none" stroke="currentColor" stroke-width="1.6"/></svg>Supply of bacterial tablet</li>
    <li><svg viewBox="0 0 16 16"><rect x="1" y="1" width="14" height="14" fill="none" stroke="currentColor" stroke-width="1.4"/><path d="M4 8l3 3 6-8" fill="none" stroke="currentColor" stroke-width="1.6"/></svg>Inspect overall condition of unit</li>
    <li><svg viewBox="0 0 16 16"><rect x="1" y="1" width="14" height="14" fill="none" stroke="currentColor" stroke-width="1.4"/><path d="M4 8l3 3 6-8" fill="none" stroke="currentColor" stroke-width="1.6"/></svg>Any repairs if required will be quoted</li>
  </ul>

  <div class="unit-art" role="img" aria-label="Wall-mounted air conditioner blowing cool air with green leaves drifting in the airflow"></div>

  <svg class="base-shapes" width="894" height="1200" viewBox="0 0 894 1200" aria-hidden="true">
    <defs>
      <linearGradient id="orangeFill" x1="0" y1="0" x2="1" y2="0">
        <stop offset="0" stop-color="#e8663a"/>
        <stop offset="1" stop-color="#f4b03c"/>
      </linearGradient>
      <linearGradient id="blueBand" x1="0" y1="0" x2="1" y2="0">
        <stop offset="0" stop-color="#14388f"/>
        <stop offset="0.5" stop-color="#2a8ce6"/>
        <stop offset="1" stop-color="#14388f"/>
      </linearGradient>
    </defs>
    <path d="M0,990 Q447,780 894,990 L894,1200 L0,1200 Z" fill="url(#orangeFill)"/>
    <path d="M0,933 Q447,785 894,933 L894,965 Q447,800 0,990 Z" fill="url(#blueBand)"/>
    <path d="M450,874 Q700,868 894,962 L894,1060 C700,1112 490,1040 450,874 Z" fill="#ffffff"/>
  </svg>

  <div class="brand"><span class="brand__dot"></span><span>Harbourline Gas &amp; Plumbing</span></div>

  <div class="contact-art" role="img" aria-label="Line icon of a tradesperson with a wrench at a service unit"></div>
  <div class="contact-tab">CONTACT US</div>
  <div class="contact-lines">
    <p class="contact-line contact-line--phone"><svg viewBox="0 0 24 24"><circle cx="12" cy="12" r="12" fill="#fff"/><path d="M8 6l2.2 0 1 3-1.5 1.2a8 8 0 0 0 4 4l1.2-1.5 3 1v2.2c0 .8-.7 1.3-1.4 1.2A11 11 0 0 1 6.8 7.4C6.7 6.7 7.2 6 8 6z" fill="#e97a3a"/></svg>0455123987</p>
    <p class="contact-line contact-line--email"><svg viewBox="0 0 24 24"><circle cx="12" cy="12" r="12" fill="#fff"/><rect x="6" y="8" width="12" height="9" rx="1" fill="none" stroke="#e97a3a" stroke-width="1.6"/><path d="M6.5 8.5l5.5 4.5 5.5-4.5" fill="none" stroke="#e97a3a" stroke-width="1.6"/></svg>admin@harbourlinegas.com.au</p>
    <p class="contact-line contact-line--abn">ABN 48120556903</p>
  </div>
</main>
</body>
</html>
```